Quietly Orchard Honey Labels

We are an importer and distributor in the UK of fine foods from Spain. We sell primarily to the retail and wholesale trade. I need a design for wrap around labels to put on jars for four different varieties of honey - Creamy Spring Blossom, Lavender, Wild Forest and Wild Thyme. The honey originates from Spain and will primarily be sold online and to independent retailers. The look and feeling I am looking for is classical, traditional, artisan and natural. I am looking for something simple and not too fussy. There needs to be an immediate obvious distinction on each label between the 4 varieties of honey, ideally by the use of different colours in some way in each design, though I would prefer the label background to be predominantly white. It is not necessary in the design to make it evident that it is from Spain. I have attached images of the jars and the honeys and also an image of the current label just for reference (but do not refer to the design). I have also attached the text for each variety of honey. The measurements for the labels are as follows: 167mm wide and 82mm high. Our logo will go on top of the lid of the jar. I really like the design I have attached to my brief. It is labelled 'Honey Design'.

Target Market(s)

Independent food retailers and online consumers

Industry/Entity Type

Fine Foods

Font styles to use
Script
Other font styles liked:
• Freeland Font for the word Honey

Requirements
Must have
• It needs to be immediately obvious by sight that each of the 4 varieties of honey are different
Nice to have
• Just the one same icon on each label for each variety of honey. Simple. Not too fussy. I really like the design attached labelled 'honey font'.

```html
<!DOCTYPE html>
<html lang="en">
<head>
<meta charset="utf-8">
<title>Quietly Orchard Honey Labels</title>
<link rel="stylesheet" href="https://fonts.googleapis.com/css2?family=Josefin+Sans:wght@700&family=Roboto+Condensed:wght@400;700&family=Arimo:wght@400&family=Roboto:wght@400&display=swap">
<style>
  :root {
    --ink: #111111;
    --paper: #ffffff;
    --honey: #f5c75b;
    --honey-soft: #f9dc94;
    --blossom: #e8b4a8;
    --blossom-edge: #f0c9bf;
    --thyme: #f68b3c;
    --thyme-edge: #f9a060;
    --forest: #f47c7b;
    --forest-edge: #f7999a;
    --lavender: #f8b783;
    --rule: #555555;
  }
  * { margin: 0; padding: 0; box-sizing: border-box; }
  html, body { width: 1200px; height: 924px; overflow: hidden; background: var(--paper); }
  body { position: relative; color: var(--ink); font-family: "Arimo", Arial, sans-serif; }

  /* lids */
  .lid { position: absolute; top: 0; width: 200px; height: 200px; border-radius: 50%;
         border: 16px solid var(--tone); display: flex; align-items: center; justify-content: center; }
  .lid-name { font-family: "Arimo", Arial, sans-serif; font-size: 17px; color: var(--ink); text-align: center; line-height: 1.2; }
  .lid-caption { position: absolute; top: 219px; width: 260px; text-align: center;
                 font-family: "Roboto", Arial, sans-serif; font-size: 13px; letter-spacing: 1.3px; }

  /* crop marks */
  .crop { position: absolute; background: var(--rule); }
  .crop.v { width: 0.6px; }
  .crop.h { height: 0.6px; }

  /* wrap-around label */
  .label { position: absolute; width: 528px; height: 259px; border: 1px solid var(--ink);
           border-radius: 22px; background: var(--paper); overflow: hidden; }
  .drip-band { position: absolute; left: 144px; top: 0; width: 247px; height: 42px;
               background: linear-gradient(to bottom, var(--honey) 0%, var(--honey) 35%, var(--honey-soft) 100%); }

  .nutrition { position: absolute; left: 16px; top: 17px; width: 107px;
               font-family: "Roboto Condensed", Arial, sans-serif; font-size: 7px; border-top: 1px solid var(--ink); }
  .nutrition-title { font-weight: 700; font-size: 6px; padding: 4px 0 2px; border-bottom: 1px solid var(--ink); }
  .nutrition-row { display: flex; justify-content: space-between; height: 13.4px; align-items: center;
                   border-bottom: 0.7px solid var(--ink); }
  .nutrition-row.sub span:first-child { padding-left: 4px; }

  .batch-box { position: absolute; left: 17px; top: 202px; width: 105px; height: 40px;
               border: 0.8px solid var(--ink); font-size: 7px; padding: 8px 0 0 8px; line-height: 15px; }

  .badge { position: absolute; left: 165px; top: 60px; width: 208px; height: 148px; }
  .badge-text { font-family: "Josefin Sans", Arial, sans-serif; font-weight: 700; fill: var(--ink); }

  .net-weight { position: absolute; left: 169px; width: 200px; top: 231px; text-align: center; font-size: 9px; }

  .story { position: absolute; left: 407px; top: 15px; width: 104px;
           font-family: "Roboto Condensed", Arial, sans-serif; font-size: 6.1px; line-height: 9px; }
  .brand { position: absolute; left: 408px; top: 118px; font-size: 11px; color: var(--ink); }
  .address { position: absolute; left: 408px; top: 155px; font-size: 8px; line-height: 9.3px; }
  .contact { position: absolute; left: 407px; top: 200px; font-size: 8px; line-height: 9.8px; }
  .origin { position: absolute; left: 407px; top: 228px; font-size: 8px; line-height: 9.3px; }
</style>
</head>
<body>

  <div class="lid" style="left:58px; --tone: var(--blossom);"><span class="lid-name">Quietly<br>Orchard</span></div>
  <div class="lid" style="left:348px; --tone: var(--thyme);"><span class="lid-name">Quietly<br>Orchard</span></div>
  <div class="lid" style="left:648px; --tone: var(--forest);"><span class="lid-name">Quietly<br>Orchard</span></div>
  <div class="lid" style="left:938px; --tone: var(--lavender);"><span class="lid-name">Quietly<br>Orchard</span></div>
  <div class="lid-caption" style="left:26px;">CREAMY SPRING BLOSSOM TOP LID</div>
  <div class="lid-caption" style="left:322px;">WILD THYME TOP LID</div>
  <div class="lid-caption" style="left:622px;">WILD FOREST TOP LID</div>
  <div class="lid-caption" style="left:900px;">LAVENDER TOP LID</div>

  <div class="crop v" style="left:60px; top:248px; height:40px;"></div>
  <div class="crop v" style="left:588px; top:248px; height:40px;"></div>
  <div class="crop v" style="left:612px; top:248px; height:40px;"></div>
  <div class="crop v" style="left:1140px; top:248px; height:40px;"></div>
  <div class="crop v" style="left:60px; top:572px; height:30px;"></div>
  <div class="crop v" style="left:588px; top:572px; height:30px;"></div>
  <div class="crop v" style="left:612px; top:572px; height:30px;"></div>
  <div class="crop v" style="left:1140px; top:572px; height:30px;"></div>
  <div class="crop v" style="left:60px; top:884px; height:40px;"></div>
  <div class="crop v" style="left:588px; top:884px; height:40px;"></div>
  <div class="crop v" style="left:612px; top:884px; height:40px;"></div>
  <div class="crop v" style="left:1140px; top:884px; height:40px;"></div>
  <div class="crop h" style="left:0; top:309px; width:40px;"></div>
  <div class="crop h" style="left:0; top:568px; width:40px;"></div>
  <div class="crop h" style="left:0; top:604px; width:40px;"></div>
  <div class="crop h" style="left:0; top:863px; width:40px;"></div>
  <div class="crop h" style="left:1160px; top:309px; width:40px;"></div>
  <div class="crop h" style="left:1160px; top:568px; width:40px;"></div>
  <div class="crop h" style="left:1160px; top:604px; width:40px;"></div>
  <div class="crop h" style="left:1160px; top:863px; width:40px;"></div>
  <div class="crop h" style="left:570px; top:309px; width:40px;"></div>
  <div class="crop h" style="left:570px; top:568px; width:40px;"></div>
  <div class="crop h" style="left:570px; top:604px; width:40px;"></div>
  <div class="crop h" style="left:570px; top:863px; width:40px;"></div>

  <!-- Creamy Spring Blossom -->
  <section class="label" style="left:60px; top:309px;">
    <div class="drip-band" role="img" aria-label="Dripping honey border along the top edge"></div>
    <div class="nutrition">
      <div class="nutrition-title">NUTRITIONAL INFORMATION per 100g</div>
      <div class="nutrition-row"><span>Energy</span><span>1394 kj / 328 kcal</span></div>
      <div class="nutrition-row"><span>Fat</span><span>&lt;0.10g</span></div>
      <div class="nutrition-row sub"><span>Of which saturated</span><span>&lt;0.10g</span></div>
      <div class="nutrition-row"><span>Carbohydrate</span><span>82g</span></div>
      <div class="nutrition-row sub"><span>Of which sugar</span><span>80.6g</span></div>
      <div class="nutrition-row"><span>Protein</span><span>&lt;0.5g</span></div>
      <div class="nutrition-row"><span>Salt</span><span>0.017g</span></div>
    </div>
    <div class="batch-box">BEST BEFORE:<br>BATCH NO:</div>
    <svg class="badge" viewBox="0 0 208 148">
      <rect x="3" y="3" width="202" height="142" rx="62" fill="var(--blossom)" stroke="var(--blossom-edge)" stroke-width="3"/>
      <path id="arc-blossom-1" d="M24 58 Q104 10 184 58" fill="none"/>
      <path id="arc-blossom-2" d="M44 72 Q104 50 164 72" fill="none"/>
      <path id="arc-blossom-h" d="M55 116 Q104 145 153 116" fill="none"/>
      <text class="badge-text" font-size="19"><textPath href="#arc-blossom-1" startOffset="50%" text-anchor="middle">CREAMY SPRING</textPath></text>
      <text class="badge-text" font-size="21"><textPath href="#arc-blossom-2" startOffset="50%" text-anchor="middle">BLOSSOM</textPath></text>
      <line x1="40" y1="86" x2="168" y2="86" stroke="var(--ink)" stroke-width="1.5"/>
      <rect x="88" y="80" width="32" height="32" rx="14" fill="#2a2a2a" role="img" aria-label="Honeybee emblem"/>
      <text class="badge-text" font-size="20"><textPath href="#arc-blossom-h" startOffset="50%" text-anchor="middle">HONEY</textPath></text>
    </svg>
    <div class="net-weight">Net weight: 450g</div>
    <p class="story">Three generations of expert beekeeping go into producing this 100% pure and creamy, multi floral spring blossom honey on a traditional apiary nestled in the wild highlands of Aragón, Spain. Master bee-keeper Mateo Lorenzana and his family carefully nurture and manage over 3000 hives of healthy honeybees to produce all natural honey at its very best.</p>
    <div class="brand">Quietly Orchard</div>
    <div class="address">WEST HOLLOWMEAD<br>MARLOWBRIDGE<br>ZX9 4QP<br>UK</div>
    <div class="contact">Tel: 01632 960412<br>sales@quietly-orchard.com</div>
    <div class="origin">PRODUCT OF SPAIN<br>23.1828/Z</div>
  </section>

  <!-- Lavender -->
  <section class="label" style="left:612px; top:309px;">
    <div class="drip-band" role="img" aria-label="Dripping honey border along the top edge"></div>
    <div class="nutrition">
      <div class="nutrition-title">NUTRITIONAL INFORMATION per 100g</div>
      <div class="nutrition-row"><span>Energy</span><span>1394 kj / 328 kcal</span></div>
      <div class="nutrition-row"><span>Fat</span><span>&lt;0.10g</span></div>
      <div class="nutrition-row sub"><span>Of which saturated</span><span>&lt;0.10g</span></div>
      <div class="nutrition-row"><span>Carbohydrate</span><span>82g</span></div>
      <div class="nutrition-row sub"><span>Of which sugar</span><span>80.6g</span></div>
      <div class="nutrition-row"><span>Protein</span><span>&lt;0.5g</span></div>
      <div class="nutrition-row"><span>Salt</span><span>0.017g</span></div>
    </div>
    <div class="batch-box">BEST BEFORE:<br>BATCH NO:</div>
    <svg class="badge" viewBox="0 0 208 148">
      <rect x="3" y="3" width="202" height="142" rx="62" fill="var(--lavender)" stroke="var(--ink)" stroke-width="1.2"/>
      <path id="arc-lavender" d="M22 74 Q104 24 186 74" fill="none"/>
      <path id="arc-lavender-h" d="M55 116 Q104 145 153 116" fill="none"/>
      <text class="badge-text" font-size="27"><textPath href="#arc-lavender" startOffset="50%" text-anchor="middle">LAVENDER</textPath></text>
      <line x1="40" y1="86" x2="168" y2="86" stroke="var(--ink)" stroke-width="1.5"/>
      <rect x="88" y="80" width="32" height="32" rx="14" fill="#2a2a2a" role="img" aria-label="Honeybee emblem"/>
      <text class="badge-text" font-size="20"><textPath href="#arc-lavender-h" startOffset="50%" text-anchor="middle">HONEY</textPath></text>
    </svg>
    <div class="net-weight">Net weight: 450g</div>
    <p class="story">Three generations of expert beekeeping go into producing this 100% pure and creamy, multi floral spring blossom honey on a traditional apiary nestled in the wild highlands of Aragón, Spain. Master bee-keeper Mateo Lorenzana and his family carefully nurture and manage over 3000 hives of healthy honeybees to produce all natural honey at its very best.</p>
    <div class="brand">Quietly Orchard</div>
    <div class="address">WEST HOLLOWMEAD<br>MARLOWBRIDGE<br>ZX9 4QP<br>UK</div>
    <div class="contact">Tel: 01632 960412<br>sales@quietly-orchard.com</div>
    <div class="origin">PRODUCT OF SPAIN<br>23.1828/Z</div>
  </section>

  <!-- Wild Thyme -->
  <section class="label" style="left:60px; top:604px;">
    <div class="drip-band" role="img" aria-label="Dripping honey border along the top edge"></div>
    <div class="nutrition">
      <div class="nutrition-title">NUTRITIONAL INFORMATION per 100g</div>
      <div class="nutrition-row"><span>Energy</span><span>1394 kj / 328 kcal</span></div>
      <div class="nutrition-row"><span>Fat</span><span>&lt;0.10g</span></div>
      <div class="nutrition-row sub"><span>Of which saturated</span><span>&lt;0.10g</span></div>
      <div class="nutrition-row"><span>Carbohydrate</span><span>82g</span></div>
      <div class="nutrition-row sub"><span>Of which sugar</span><span>80.6g</span></div>
      <div class="nutrition-row"><span>Protein</span><span>&lt;0.5g</span></div>
      <div class="nutrition-row"><span>Salt</span><span>0.017g</span></div>
    </div>
    <div class="batch-box">BEST BEFORE:<br>BATCH NO:</div>
    <svg class="badge" viewBox="0 0 208 148">
      <rect x="3" y="3" width="202" height="142" rx="62" fill="var(--thyme)" stroke="var(--thyme-edge)" stroke-width="3"/>
      <path id="arc-thyme" d="M22 74 Q104 24 186 74" fill="none"/>
      <path id="arc-thyme-h" d="M55 116 Q104 145 153 116" fill="none"/>
      <text class="badge-text" font-size="25"><textPath href="#arc-thyme" startOffset="50%" text-anchor="middle">WILD THYME</textPath></text>
      <line x1="40" y1="86" x2="168" y2="86" stroke="var(--ink)" stroke-width="1.5"/>
      <rect x="88" y="80" width="32" height="32" rx="14" fill="#2a2a2a" role="img" aria-label="Honeybee emblem"/>
      <text class="badge-text" font-size="20"><textPath href="#arc-thyme-h" startOffset="50%" text-anchor="middle">HONEY</textPath></text>
    </svg>
    <div class="net-weight">Net weight: 450g</div>
    <p class="story">Three generations of expert beekeeping go into producing this 100% pure and creamy, multi floral spring blossom honey on a traditional apiary nestled in the wild highlands of Aragón, Spain. Master bee-keeper Mateo Lorenzana and his family carefully nurture and manage over 3000 hives of healthy honeybees to produce all natural honey at its very best.</p>
    <div class="brand">Quietly Orchard</div>
    <div class="address">WEST HOLLOWMEAD<br>MARLOWBRIDGE<br>ZX9 4QP<br>UK</div>
    <div class="contact">Tel: 01632 960412<br>sales@quietly-orchard.com</div>
    <div class="origin">PRODUCT OF SPAIN<br>23.1828/Z</div>
  </section>

  <!-- Wild Forest -->
  <section class="label" style="left:612px; top:604px;">
    <div class="drip-band" role="img" aria-label="Dripping honey border along the top edge"></div>
    <div class="nutrition">
      <div class="nutrition-title">NUTRITIONAL INFORMATION per 100g</div>
      <div class="nutrition-row"><span>Energy</span><span>1394 kj / 328 kcal</span></div>
      <div class="nutrition-row"><span>Fat</span><span>&lt;0.10g</span></div>
      <div class="nutrition-row sub"><span>Of which saturated</span><span>&lt;0.10g</span></div>
      <div class="nutrition-row"><span>Carbohydrate</span><span>82g</span></div>
      <div class="nutrition-row sub"><span>Of which sugar</span><span>80.6g</span></div>
      <div class="nutrition-row"><span>Protein</span><span>&lt;0.5g</span></div>
      <div class="nutrition-row"><span>Salt</span><span>0.017g</span></div>
    </div>
    <div class="batch-box">BEST BEFORE:<br>BATCH NO:</div>
    <svg class="badge" viewBox="0 0 208 148">
      <rect x="3" y="3" width="202" height="142" rx="62" fill="var(--forest)" stroke="var(--forest-edge)" stroke-width="3"/>
      <path id="arc-forest" d="M22 74 Q104 24 186 74" fill="none"/>
      <path id="arc-forest-h" d="M55 116 Q104 145 153 116" fill="none"/>
      <text class="badge-text" font-size="24"><textPath href="#arc-forest" startOffset="50%" text-anchor="middle">WILD FOREST</textPath></text>
      <line x1="40" y1="86" x2="168" y2="86" stroke="var(--ink)" stroke-width="1.5"/>
      <rect x="88" y="80" width="32" height="32" rx="14" fill="#2a2a2a" role="img" aria-label="Honeybee emblem"/>
      <text class="badge-text" font-size="20"><textPath href="#arc-forest-h" startOffset="50%" text-anchor="middle">HONEY</textPath></text>
    </svg>
    <div class="net-weight">Net weight: 450g</div>
    <p class="story">Three generations of expert beekeeping go into producing this 100% pure and creamy, multi floral spring blossom honey on a traditional apiary nestled in the wild highlands of Aragón, Spain. Master bee-keeper Mateo Lorenzana and his family carefully nurture and manage over 3000 hives of healthy honeybees to produce all natural honey at its very best.</p>
    <div class="brand">Quietly Orchard</div>
    <div class="address">WEST HOLLOWMEAD<br>MARLOWBRIDGE<br>ZX9 4QP<br>UK</div>
    <div class="contact">Tel: 01632 960412<br>sales@quietly-orchard.com</div>
    <div class="origin">PRODUCT OF SPAIN<br>23.1828/Z</div>
  </section>

</body>
</html>
```